Terravane Business Card Design

We need a modern, clean, business card design for our hardscape solution company. I have outlined our specialist areas in the card information section. We meet and greet and wish to build relationships with large-scale builders and project managers of large-scale building companies. Hence the reason for the business card.We want them to understand we are their 'solution' and we will make their working life easier and less stressful. We also are the highest quality construction with an exceptional eye for detail taking a lot of pressure off the project managers. I have done a few mock-ups myself but would like to see what else can be created. We are open to black or white (or grey) background.

Industry/Entity Type

Construction

Contact Information for Business Card

Mark Hollis - Director
0471 583 905
mark@terravanegroup.com

www.terravanegroup.com.au

"Hardscape Construction Solutions for Large-Scale Builders" (front)

Logo already designed and to be added.

REAR:

Your One-Stop Hardscape Solution For:

Retirement Village & Community Development Construction

- Synthetic Sports Fields - Bowling Greens
- Tennis Courts - Concreting
- Paving - Landscape

www.terravanegroup.com

```html
<!DOCTYPE html>
<html lang="en">
<head>
<meta charset="utf-8">
<title>Terravane Business Card</title>
<link href="https://fonts.googleapis.com/css2?family=Play:wght@400;700&display=swap" rel="stylesheet">
<style>
  :root {
    --bg: #d9d9d9;
    --card: #ffffff;
    --green: #a2bb16;
    --blue: #0d8fd1;
    --ink: #3d3d3d;
    --muted: #8a8a8a;
  }
  * { margin: 0; padding: 0; box-sizing: border-box; }
  html, body { width: 1200px; height: 894px; overflow: hidden; }
  body {
    background: var(--bg);
    font-family: "Play", sans-serif;
    color: var(--ink);
    position: relative;
  }
  .card {
    position: absolute;
    background: var(--card);
    box-shadow: 0 6px 18px rgba(0,0,0,0.18);
    overflow: hidden;
  }
  .card-back { left: 560px; top: 50px; width: 580px; height: 331px; }
  .card-front { left: 60px; top: 410px; width: 760px; height: 434px; }

  .brand {
    display: flex;
    align-items: center;
    gap: 10px;
    color: var(--green);
    font-weight: 700;
    letter-spacing: -0.5px;
    white-space: nowrap;
  }
  .brand-dot {
    border-radius: 50%;
    background: var(--blue);
    flex: none;
  }

  /* Rear */
  .back-content {
    position: absolute;
    inset: 0;
    display: flex;
    flex-direction: column;
    align-items: center;
    justify-content: center;
    text-align: center;
  }
  .card-back .brand { font-size: 48px; }
  .card-back .brand-dot { width: 20px; height: 20px; }
  .services-intro {
    margin-top: 18px;
    font-size: 14px;
    font-weight: 700;
    color: var(--ink);
  }
  .services-focus {
    margin-top: 4px;
    font-size: 13px;
    color: var(--blue);
  }
  .services-list {
    margin-top: 10px;
    list-style: none;
    display: grid;
    grid-template-columns: repeat(3, auto);
    gap: 4px 22px;
    font-size: 12px;
    color: var(--ink);
  }
  .services-list li::before {
    content: "";
    display: inline-block;
    width: 7px; height: 7px;
    background: var(--green);
    margin-right: 6px;
    vertical-align: 1px;
  }
  .back-web {
    margin-top: 14px;
    font-size: 13px;
    color: var(--muted);
    letter-spacing: 0.5px;
  }

  /* Front */
  .card-front .brand { position: absolute; left: 110px; top: 34px; font-size: 50px; }
  .card-front .brand-dot { width: 18px; height: 18px; }

  .block-green {
    position: absolute;
    left: 96px; top: 104px;
    width: 150px; height: 76px;
    background: var(--green);
  }
  .band-blue {
    position: absolute;
    left: 252px; top: 184px;
    width: 508px; height: 86px;
    background: var(--blue);
    display: flex; align-items: center; justify-content: center;
    padding: 0 16px;
  }
  .band-blue .tagline {
    color: #fff;
    font-size: 15px;
    letter-spacing: 0.3px;
    text-align: center;
    white-space: nowrap;
  }

  .person {
    position: absolute;
    left: 520px; top: 112px;
  }
  .person .name {
    color: var(--green);
    font-size: 22px;
    letter-spacing: 1px;
    line-height: 1;
  }
  .person .role {
    font-size: 14px;
    letter-spacing: 1.5px;
    margin-top: 4px;
  }

  .contact-list {
    position: absolute;
    list-style: none;
    font-size: 13px;
  }
  .contact-list li {
    display: flex; align-items: center; gap: 10px;
    height: 24px;
    white-space: nowrap;
  }
  .contact-list .icon {
    width: 16px; height: 16px;
    background: var(--green);
    flex: none;
    display: flex; align-items: center; justify-content: center;
  }
  .contact-list .icon svg { width: 10px; height: 10px; }
  .contact-left { left: 34px; top: 196px; }
  .contact-social { left: 432px; top: 324px; }
</style>
</head>
<body>

  <section class="card card-back" aria-label="Card back">
    <div class="back-content">
      <div class="brand"><span class="brand-dot"></span>Terravane</div>
      <p class="services-intro">Your One-Stop Hardscape Solution For:</p>
      <p class="services-focus">Retirement Village &amp; Community Development Construction</p>
      <ul class="services-list">
        <li>Synthetic Sports Fields</li>
        <li>Bowling Greens</li>
        <li>Tennis Courts</li>
        <li>Concreting</li>
        <li>Paving</li>
        <li>Landscape</li>
      </ul>
      <p class="back-web">www.terravanegroup.com</p>
    </div>
  </section>

  <section class="card card-front" aria-label="Card front">
    <div class="brand"><span class="brand-dot"></span>Terravane</div>

    <div class="block-green"></div>

    <div class="person">
      <div class="name">MARK HOLLIS</div>
      <div class="role">DIRECTOR</div>
    </div>

    <div class="band-blue">
      <span class="tagline">Hardscape Construction Solutions for Large-Scale Builders</span>
    </div>

    <ul class="contact-list contact-left">
      <li>
        <span class="icon"><svg viewBox="0 0 10 10"><path d="M2 1l2 2-1 1.2c.6 1.2 1.6 2.2 2.8 2.8L7 6l2 2-1.3 1.3C4.5 9 1 5.5 0.7 2.3z" fill="#fff"/></svg></span>
        0471 583 905
      </li>
      <li>
        <span class="icon"><svg viewBox="0 0 10 10"><rect x="1" y="2.5" width="8" height="5" fill="none" stroke="#fff" stroke-width="1"/><path d="M1 2.5l4 3 4-3" fill="none" stroke="#fff" stroke-width="1"/></svg></span>
        mark@terravanegroup.com
      </li>
      <li>
        <span class="icon"><svg viewBox="0 0 10 10"><circle cx="5" cy="5" r="3.8" fill="none" stroke="#fff" stroke-width="1"/><path d="M1.2 5h7.6M5 1.2v7.6" stroke="#fff" stroke-width="0.8"/></svg></span>
        www.terravanegroup.com.au
      </li>
    </ul>

    <ul class="contact-list contact-social">
      <li>
        <span class="icon"><svg viewBox="0 0 10 10"><circle cx="5" cy="5" r="3.8" fill="none" stroke="#fff" stroke-width="1"/><path d="M1.2 5h7.6M5 1.2v7.6" stroke="#fff" stroke-width="0.8"/></svg></span>
        www.terravanegroup.com
      </li>
      <li>
        <span class="icon"></span>
        www.chirpline.com
      </li>
      <li>
        <span class="icon"></span>
        www.friendwall.com
      </li>
    </ul>
  </section>

</body>
</html>
```